Animated Banner Ads

We need 4 Banner Ads that interchange with the banner ad of the same size as per attached images. We also would like the 'Free Quote' icon to flash. The design is already done, we just need someone to be able to make these interchange to be able to use as Google Adsense ads and banner ads. I have attached the .jpg and .psd files. We are open to the designer coming up with a better design though and if we like it we will go with you. We are a drafting company targeting Perth and our companies main benefits are affordable, quick turn-around, local, excellent designs and guarantee council approval.

```html
<!DOCTYPE html>
<html lang="en">
<head>
<meta charset="utf-8">
<title>Planwright – Animated Banner Ads</title>
<link rel="stylesheet" href="https://fonts.googleapis.com/css2?family=Arimo:wght@400;700&family=Noto+Sans:wght@700&family=Kaushan+Script&display=swap">
<style>
  :root {
    --board: #333333;
    --label: #ffffff;
    --header-bg: #ffffff;
    --header-ink: #3c3c3c;
    --brand: #1a7fd8;
    --brand-mark: #9a9a9a;
    --before-bg: #0b7ee0;
    --after-light: #34c0f0;
    --after-deep: #0f86dc;
    --text-light: #ffffff;
    --before-btn: #ff69b4;
    --before-btn-ink: #5b3b4c;
    --after-btn: #e014e6;
    --after-btn-dark: #b20cb8;
  }
  * { box-sizing: border-box; margin: 0; padding: 0; }
  html, body { width: 1200px; height: 808px; overflow: hidden; background: var(--board); }
  .board { position: relative; width: 1200px; height: 808px; }

  .stage-label {
    position: absolute;
    font-family: "Kaushan Script", cursive;
    font-size: 46px;
    color: var(--label);
    line-height: 1;
  }
  .stage-label--before { left: 348px; top: 32px; }
  .stage-label--after { left: 738px; top: 32px; }
  .stage-label--animated { left: 932px; top: 468px; }

  .pointer { position: absolute; left: 930px; top: 380px; }

  .banner {
    position: absolute;
    width: 403px; height: 338px;
    overflow: hidden;
    font-family: "Arimo", sans-serif;
    color: var(--text-light);
    text-align: center;
    transform-origin: top left;
  }
  .banner--before { left: 215px; top: 107px; background: var(--before-bg); }
  .banner--after, .banner--frame {
    background: radial-gradient(ellipse 70% 60% at 50% 42%, var(--after-light), var(--after-deep) 100%);
  }
  .banner--after { left: 618px; top: 107px; }
  .banner--frame { top: 541px; transform: scale(0.722); }
  .banner--frame-1 { left: 119px; }
  .banner--frame-2 { left: 462px; }
  .banner--frame-3 { left: 805px; }

  .banner__header {
    height: 66px; background: var(--header-bg);
    display: flex; align-items: center; justify-content: space-between;
    padding: 0 12px 0 10px;
  }
  .brand { display: flex; align-items: center; gap: 8px; }
  .brand__mark { width: 30px; height: 30px; background: var(--brand-mark); }
  .brand__name { font-family: "Arimo", sans-serif; font-weight: 700; font-size: 25px; color: var(--brand); }
  .service { font-weight: 700; font-size: 17px; line-height: 1.17; color: var(--header-ink); }

  .tagline { margin-top: 12px; font-size: 15px; letter-spacing: 0.2px; }
  .headline {
    margin-top: 10px;
    font-family: "Noto Sans", sans-serif; font-weight: 700;
    font-size: 32px; line-height: 38px;
  }
  .cue { margin-top: 14px; font-size: 13px; font-weight: 700; }
  .quote-btn {
    position: relative; overflow: hidden;
    width: 251px; height: 43px; margin: 8px auto 0;
    border-radius: 10px;
    display: flex; align-items: center; justify-content: center;
    font-weight: 700; font-size: 22px; letter-spacing: 0.5px;
  }
  .banner--before .quote-btn { background: var(--before-btn); color: var(--before-btn-ink); }
  .banner--after .quote-btn, .banner--frame .quote-btn {
    background: linear-gradient(to bottom, var(--after-btn) 0 55%, var(--after-btn-dark) 100%);
    color: var(--text-light);
  }
  .quote-btn__label { position: relative; z-index: 1; }
  .quote-btn__sheen {
    position: absolute; top: 0; bottom: 0; width: 110px;
    background: linear-gradient(to right, rgba(255,255,255,0), rgba(255,255,255,0.95) 50%, rgba(255,255,255,0));
    z-index: 2;
  }
  .banner--frame-1 .quote-btn__sheen { left: -20px; }
  .banner--frame-2 .quote-btn__sheen { left: 110px; }
  .banner--frame-3 .quote-btn__sheen { left: 170px; }
  .response { margin-top: 10px; font-size: 13px; }
</style>
</head>
<body>
<div class="board">
  <span class="stage-label stage-label--before">Before</span>
  <span class="stage-label stage-label--after">After</span>
  <span class="stage-label stage-label--animated">Animated</span>

  <svg class="pointer" width="80" height="90" viewBox="0 0 80 90" aria-hidden="true">
    <path d="M66 80 C 60 50, 40 30, 16 16" fill="none" stroke="#ffffff" stroke-width="4" stroke-linecap="round"/>
    <path d="M10 12 L30 14 L18 28 Z" fill="#ffffff"/>
  </svg>

  <!-- Static design -->
  <section class="banner banner--before">
    <header class="banner__header">
      <div class="brand"><span class="brand__mark"></span><span class="brand__name">Planwright</span></div>
      <div class="service">Architectural Design<br>Drafting Services</div>
    </header>
    <p class="tagline">PROFESSIONAL - FAST TURNAROUND - AFFORDABLE</p>
    <h2 class="headline">NEED DRAWINGS<br>FOR<br>COUNCIL APPROVAL?</h2>
    <p class="cue">CLICK!</p>
    <div class="quote-btn"><span class="quote-btn__label">FREE QUOTE</span></div>
    <p class="response">WE RESPOND WITHIN 0-24HRS</p>
  </section>

  <!-- Refreshed design -->
  <section class="banner banner--after">
    <header class="banner__header">
      <div class="brand"><span class="brand__mark"></span><span class="brand__name">Planwright</span></div>
      <div class="service">Architectural Design<br>Drafting Services</div>
    </header>
    <p class="tagline">PROFESSIONAL - FAST TURNAROUND - AFFORDABLE</p>
    <h2 class="headline">NEED DRAWINGS<br>FOR<br>COUNCIL APPROVAL?</h2>
    <p class="cue">CLICK!</p>
    <div class="quote-btn"><span class="quote-btn__label">FREE QUOTE</span></div>
    <p class="response">WE RESPOND WITHIN 0-24HRS</p>
  </section>

  <!-- Animation frames -->
  <section class="banner banner--frame banner--frame-1">
    <header class="banner__header">
      <div class="brand"><span class="brand__mark"></span><span class="brand__name">Planwright</span></div>
      <div class="service">Architectural Design<br>Drafting Services</div>
    </header>
    <p class="tagline">PROFESSIONAL - FAST TURNAROUND - AFFORDABLE</p>
    <h2 class="headline">NEED DRAWINGS<br>FOR<br>COUNCIL APPROVAL?</h2>
    <p class="cue">CLICK!</p>
    <div class="quote-btn"><span class="quote-btn__label">FREE QUOTE</span><span class="quote-btn__sheen"></span></div>
    <p class="response">WE RESPOND WITHIN 0-24HRS</p>
  </section>

  <section class="banner banner--frame banner--frame-2">
    <header class="banner__header">
      <div class="brand"><span class="brand__mark"></span><span class="brand__name">Planwright</span></div>
      <div class="service">Architectural Design<br>Drafting Services</div>
    </header>
    <p class="tagline">PROFESSIONAL - FAST TURNAROUND - AFFORDABLE</p>
    <h2 class="headline">NEED DRAWINGS<br>FOR<br>COUNCIL APPROVAL?</h2>
    <p class="cue">CLICK!</p>
    <div class="quote-btn"><span class="quote-btn__label">FREE QUOTE</span><span class="quote-btn__sheen"></span></div>
    <p class="response">WE RESPOND WITHIN 0-24HRS</p>
  </section>

  <section class="banner banner--frame banner--frame-3">
    <header class="banner__header">
      <div class="brand"><span class="brand__mark"></span><span class="brand__name">Planwright</span></div>
      <div class="service">Architectural Design<br>Drafting Services</div>
    </header>
    <p class="tagline">PROFESSIONAL - FAST TURNAROUND - AFFORDABLE</p>
    <h2 class="headline">NEED DRAWINGS<br>FOR<br>COUNCIL APPROVAL?</h2>
    <p class="cue">CLICK!</p>
    <div class="quote-btn"><span class="quote-btn__label">FREE QUOTE</span><span class="quote-btn__sheen"></span></div>
    <p class="response">WE RESPOND WITHIN 0-24HRS</p>
  </section>
</div>
</body>
</html>
```